We Need a New Feature/Price comparison Table For Our Site

Hello,
We offer a subscription website to our clients highlighting available Bio/Pharma assets by therapeutic area, investment case, etc... (We are an investment bank in NYC).
However we are missing some design, most notably a nice pricing table. You can see it as it exists today if you look at the first attachment (Pricingtable). You can also see this on www.quelmora.com if you click on the ad on the right. Also please browse the site so you can get a better 'feel' for it.
We want the pricing section to look much nicer, but we aren't graphic designers so we're really not sure what the best way to do this would be.
I attached some images of pricing tables from other sites that look really nice, but obviously if we copied them exactly, they wouldn't fit with our design. So please be as creative and free as possible in designing something new for us. You can use the same info as on the pricing table on our site (First attachment). But that's all that should stay the same :)
Thanks in advance,
Dwight

```html
<!DOCTYPE html>
<html lang="en">
<head>
<meta charset="utf-8">
<title>Subscription Plans</title>
<link rel="stylesheet" href="https://fonts.googleapis.com/css2?family=Arimo:wght@400;700&display=swap">
<style>
  :root {
    --page-bg: #ffffff;
    --bar-dark: #1a1a1a;
    --bar-mid: #3a3a3a;
    --row-bg: #ececec;
    --row-bg-free: #e2e2e2;
    --row-line: #ffffff;
    --row-text: #333333;
    --bullet: #8a8a8a;
    --green-1: #b7e07a;
    --green-2: #79b833;
    --blue-1: #bcd8f3;
    --blue-2: #6a9fd8;
    --pink-1: #f7c9c9;
    --pink-2: #e08c8c;
    --btn-1: #3b3b3b;
    --btn-2: #0e0e0e;
    --arrow-green: #9fd45a;
    --arrow-blue: #4d8fe0;
    --arrow-red: #e07474;
  }
  * { box-sizing: border-box; margin: 0; padding: 0; }
  html, body {
    width: 731px; height: 1200px; overflow: hidden;
    background: var(--page-bg);
    font-family: "Arimo", Arial, sans-serif;
  }
  .pricing {
    position: relative;
    width: 587px; height: 964px;
    transform: scale(1.2453);
    transform-origin: 0 0;
  }
  .plan {
    position: absolute;
    background: var(--row-bg);
  }
  .plan--free { left: 8px; top: 31px; width: 190px; background: var(--row-bg-free); }
  .plan--premium {
    left: 198px; top: 20px; width: 192px; z-index: 2;
    box-shadow: 0 0 14px rgba(0,0,0,.45);
  }
  .plan--corporate { left: 390px; top: 31px; width: 190px; }

  .plan__name {
    height: 24px; line-height: 24px;
    background: linear-gradient(#2a2a2a, var(--bar-dark));
    color: #fff; text-align: center; font-size: 17px;
  }
  .plan--premium .plan__name { height: 26px; line-height: 27px; }

  .plan__price {
    height: 90px;
    display: flex; align-items: center; justify-content: center;
    color: #fff;
    text-shadow: 0 1px 3px rgba(0,0,0,.35);
  }
  .plan--premium .plan__price { height: 99px; }
  .plan--free .plan__price { background: radial-gradient(circle at 40% 30%, var(--green-1), var(--green-2)); }
  .plan--premium .plan__price { background: radial-gradient(circle at 40% 30%, var(--blue-1), var(--blue-2)); }
  .plan--corporate .plan__price { background: radial-gradient(circle at 40% 30%, var(--pink-1), var(--pink-2)); }
  .price__currency { font-size: 26px; align-self: flex-start; margin-top: 18px; margin-right: 1px; }
  .plan--premium .price__currency { margin-top: 24px; }
  .price__amount { font-size: 52px; letter-spacing: -1px; }

  .section-title {
    height: 41px; line-height: 42px;
    background: linear-gradient(var(--bar-mid), var(--bar-dark));
    color: #fff; font-size: 15px; letter-spacing: .6px;
    padding-left: 10px;
  }
  .plan--free .section-title:nth-of-type(2) { height: 40px; }

  .features { list-style: none; }
  .feature {
    display: flex; align-items: center;
    border-bottom: 1px solid var(--row-line);
    color: var(--row-text);
    font-size: 15.5px; line-height: 16px;
    padding-left: 12px; padding-right: 4px;
  }
  .feature::before {
    content: "";
    flex: none;
    width: 0; height: 0;
    border-left: 4px solid var(--bullet);
    border-top: 3px solid transparent;
    border-bottom: 3px solid transparent;
    margin-right: 10px;
  }

  .plan__action {
    display: flex; align-items: center; justify-content: center;
  }
  .plan--free .plan__action { height: 52px; }
  .plan--premium .plan__action, .plan--corporate .plan__action { height: 59px; }
  .btn {
    position: relative;
    width: 158px; height: 26px;
    border-radius: 4px;
    background: linear-gradient(var(--btn-1), var(--btn-2));
    box-shadow: 0 1px 2px rgba(0,0,0,.4);
    color: #fff; font-size: 12px; line-height: 26px; text-align: center;
    text-decoration: none;
  }
  .btn svg { position: absolute; right: 8px; top: 5px; }
</style>
</head>
<body>
<main class="pricing">

  <section class="plan plan--free">
    <h2 class="plan__name" style="font-weight:400">Free</h2>
    <div class="plan__price"><span class="price__currency">$</span><span class="price__amount">0</span></div>
    <h3 class="section-title" style="font-weight:400">BUY SIDE FEATURES</h3>
    <ul class="features">
      <li class="feature" style="height:41px">1 Seat</li>
      <li class="feature" style="height:46px">Access Over 1,800<br>Listings</li>
      <li class="feature" style="height:45px">View Profiles of Over<br>800 Companies</li>
    </ul>
    <h3 class="section-title" style="font-weight:400">SELL SIDE FEATURES</h3>
    <ul class="features">
      <li class="feature" style="height:42px">Add 1 listing</li>
    </ul>
    <div class="plan__action">
      <a class="btn" href="#">Register
        <svg width="22" height="16" viewBox="0 0 22 16"><path d="M1 1l7 7-7 7M7 1l7 7-7 7M13 1l7 7-7 7" fill="none" stroke="var(--arrow-green)" stroke-width="2.5"/></svg>
      </a>
    </div>
  </section>

  <section class="plan plan--premium">
    <h2 class="plan__name" style="font-weight:400">Premium</h2>
    <div class="plan__price"><span class="price__currency">$</span><span class="price__amount">799</span></div>
    <h3 class="section-title" style="font-weight:400">BUY SIDE FEATURES</h3>
    <ul class="features">
      <li class="feature" style="height:40px">1 Seat</li>
      <li class="feature" style="height:46px">Access Over 1,800<br>Listings</li>
      <li class="feature" style="height:46px">View Profiles of Over<br>800 Companies</li>
      <li class="feature" style="height:47px">3 Undisclosed<br>Items/Calls per Month</li>
      <li class="feature" style="height:68px">Access of Lead<br>Contacts and<br>Messaging Capabilities</li>
      <li class="feature" style="height:47px">View Proprietary<br>Listings</li>
      <li class="feature" style="height:65px">Download<br>Non-Confidential<br>Documents</li>
      <li class="feature" style="height:52px">Export Results to<br>Excel or PDF</li>
    </ul>
    <h3 class="section-title" style="font-weight:400">SELL SIDE FEATURES</h3>
    <ul class="features">
      <li class="feature" style="height:38px">Add up to 25 listings</li>
      <li class="feature" style="height:46px">Screen Buy-Side<br>Dealmakers</li>
      <li class="feature" style="height:65px">Receice Custom<br>Sell-Side Analytics<br>(In Development)</li>
      <li class="feature" style="height:56px">50% Off Licensing<br>Pharmalink Insights</li>
    </ul>
    <div class="plan__action">
      <a class="btn" href="#">Buy
        <svg width="22" height="16" viewBox="0 0 22 16"><path d="M1 1l7 7-7 7M7 1l7 7-7 7M13 1l7 7-7 7" fill="none" stroke="var(--arrow-blue)" stroke-width="2.5"/></svg>
      </a>
    </div>
  </section>

  <section class="plan plan--corporate">
    <h2 class="plan__name" style="font-weight:400">Corporate</h2>
    <div class="plan__price"><span class="price__currency">$</span><span class="price__amount">1999</span></div>
    <h3 class="section-title" style="font-weight:400">BUY SIDE FEATURES</h3>
    <ul class="features">
      <li class="feature" style="height:40px">3 Seats</li>
      <li class="feature" style="height:46px">Access Over 1,800<br>Listings</li>
      <li class="feature" style="height:46px">View Profiles of Over<br>800 Companies</li>
      <li class="feature" style="height:47px">9 Undisclosed<br>Items/Calls per Month</li>
      <li class="feature" style="height:68px">Access of Lead<br>Contacts and<br>Messaging Capabilities</li>
      <li class="feature" style="height:47px">View Proprietary<br>Listings</li>
      <li class="feature" style="height:65px">Download<br>Non-Confidential<br>Documents</li>
      <li class="feature" style="height:52px">Export Results to<br>Excel or PDF</li>
    </ul>
    <h3 class="section-title" style="font-weight:400">SELL SIDE FEATURES</h3>
    <ul class="features">
      <li class="feature" style="height:38px">Add up to 100 listings</li>
      <li class="feature" style="height:46px">Screen Buy-Side<br>Dealmakers</li>
      <li class="feature" style="height:65px">Receice Custom<br>Sell-Side Analytics<br>(In Development)</li>
      <li class="feature" style="height:56px">50% Off Licensing<br>Pharmalink Insights</li>
    </ul>
    <div class="plan__action">
      <a class="btn" href="#">Buy
        <svg width="22" height="16" viewBox="0 0 22 16"><path d="M1 1l7 7-7 7M7 1l7 7-7 7M13 1l7 7-7 7" fill="none" stroke="var(--arrow-red)" stroke-width="2.5"/></svg>
      </a>
    </div>
  </section>

</main>
</body>
</html>
```